Medical Simulation - Creative Graphic for Data

My company needs a creative graph that depicts the rationales (or reasons) our learners chose certain drug options. Basically, our clients not only want to know how many times certain drugs were selected, but the "whys" behind their choices. I would like a PPT graphic that I can use for other deliverables, where I can simply switch out the drug (treatment) names, the "whys" (what we call rationales), and the specific metrics (percentages, "n" numbers, etc), and the graphic will update and adjust to the new information. The title of the graph (or the slide where the graph will live) should be something like "Treatment Rationales" or something to that effect. Include a placeholder for text to go if anyone wants to add an analysis of the graphic later. This placeholder should accommodate 2-3 bullet points of text. We want this graphic to not just be an image, but organized in a way that you would see in a presentation slide, with a title, place holder for analysis (as indicated above), branding colors, and helpful information to understand the graphic (what is included in this post and it's associated attachments).

I've included specific drug names, rationales, and metrics to use for this (please see excel document). If you are going to design the graph directly in PPT, please use the PPT template design included. Please don't feel like you have to use 1 slide only or can have multiple graphs, if that makes sense for you design idea. They just need to fit within the coloring of the PPT. For font, please use Arial. Below is a Google Drive Link to branding colors and vector art.

https://share.vorlintbox.net/open?id=4K2TQ8Rbm3-XpL71zNwYtH5KrcQd

We are open to many variations and design ideas. Please don't feel like you have to limit yourself! I've attached a few ideas that we've had and it may be a good place to start. We would ESPECIALLY like to see a version utilizing the radial graph (similar to the one included in the Rationales_DesignIdeas document).

Please reach out if you have any questions. Thanks!

• It would be great to see the radial graph as a design variation (see link below)
• http://4.plotwerva.com/products/plotwerva/docs/users-guide/img/Samples/radar-chart-fixed-radius.png

```html
<!DOCTYPE html>
<html lang="en">
<head>
<meta charset="utf-8">
<title>Treatment Rationales</title>
<link rel="stylesheet" href="https://fonts.googleapis.com/css2?family=Arimo:wght@400;700&display=swap">
<style>
  :root {
    --navy: #0a3a58;
    --band: #0b3d5d;
    --mid-blue: #13659c;
    --light-blue: #8ac9ea;
    --label-light-blue: #6fb8e0;
    --orange: #f79646;
    --gray: #a6a6a6;
    --dark-gray: #5a5858;
    --leader: #8c8c8c;
    --text-gray: #8a8a8a;
    --label-dark: #404040;
    --white: #ffffff;
  }
  html, body {
    margin: 0;
    padding: 0;
    width: 800px;
    height: 1200px;
    overflow: hidden;
    background: var(--white);
    font-family: "Arimo", Arial, sans-serif;
  }
  .canvas { position: relative; width: 800px; height: 1200px; }
  .slide { position: absolute; left: 8px; top: 306px; width: 784px; height: 588px; background: var(--white); }
  .top-band { position: absolute; left: 0; top: 0; width: 784px; height: 18px; background: var(--band); }
  .brand-tab {
    position: absolute; right: 0; top: 18px; width: 240px; height: 20px;
    background: linear-gradient(90deg, rgba(247,150,70,0) 0%, rgba(247,150,70,0.6) 35%, var(--orange) 70%);
    color: var(--white); font-weight: 700; font-size: 12.5px; letter-spacing: 3.2px;
    line-height: 20px; text-align: right; padding-right: 16px; box-sizing: border-box;
  }
  .rule { position: absolute; left: 0; height: 3px;
    background: linear-gradient(180deg, rgba(0,0,0,0.10), rgba(0,0,0,0)); }
  .rule--header { top: 32px; width: 560px; }
  .rule--title { top: 118px; width: 560px; }
  .slide-title {
    position: absolute; left: 0; top: 56px; width: 784px; margin: 0;
    text-align: center; color: var(--navy); font-weight: 700; font-size: 39px; letter-spacing: 0.5px;
  }
  .analysis { position: absolute; left: 521px; top: 406px; width: 236px; }
  .analysis h2 { margin: 0 0 4px; font-size: 12.5px; font-weight: 700; color: var(--navy); }
  .analysis p, .analysis li { font-size: 10px; line-height: 13px; color: var(--text-gray); margin: 0; }
  .analysis ul { margin: 0; padding-left: 14px; list-style: none; }
  .analysis li { position: relative; }
  .analysis li::before { content: "•"; position: absolute; left: -14px; }
  .bottom-band {
    position: absolute; left: 0; bottom: 0; width: 784px; height: 17px; background: var(--band);
    color: var(--white); font-size: 8.5px; line-height: 17px; text-align: center;
  }
  .chart { position: absolute; left: 0; top: 0; width: 800px; height: 1200px; }
  .chart text { font-family: "Arimo", Arial, sans-serif; }
  .seg-label { fill: var(--white); font-size: 14px; text-anchor: middle; dominant-baseline: central; }
  .call-label { font-size: 14.5px; }
  .leader { fill: none; stroke: var(--leader); stroke-width: 1.2; }
  .leader-dot { fill: var(--leader); }
</style>
</head>
<body>
<div class="canvas">
  <section class="slide">
    <div class="top-band"></div>
    <div class="brand-tab">EDUCATION</div>
    <div class="rule rule--header"></div>
    <h1 class="slide-title">TREATMENT RATIONALES</h1>
    <div class="rule rule--title"></div>

    <div class="analysis">
      <h2>Heading Here</h2>
      <p>Sed do eiusmod tempor incididunt ut labore et dolore magna aliqua. Ut enimad minim</p>
      <ul>
        <li>Duis aute irure dolor in reprehenderit in voluptate velit esse cillum</li>
        <li>dolore eu fugiat nulla pariatur. Excepteur sint occaecat cupidatat non</li>
        <li>proident, sunt inculpa qui officia deserunt mollit anim id est laborum.</li>
      </ul>
    </div>

    <div class="bottom-band">Clinora Education Confidential and Proprietary Information</div>
  </section>

  <svg class="chart" viewBox="0 0 1000 1500" role="img" aria-label="Radial chart of treatment rationales">
    <g class="segments" stroke="#ffffff" stroke-width="1.5">
      <path fill="var(--navy)" d="M500 581 A212 212 0 0 1 708.1 833.5 L551 802.9 A52 52 0 0 0 500 741 Z"/>
      <path fill="var(--gray)" d="M655.1 823.1 A158 158 0 0 1 440.8 939.5 L480.5 841.2 A52 52 0 0 0 551 802.9 Z"/>
      <path fill="var(--orange)" d="M420.6 989.6 A212 212 0 0 1 288.8 774.5 L448.2 788.5 A52 52 0 0 0 480.5 841.2 Z"/>
      <path fill="var(--light-blue)" d="M292.8 774.9 A208 208 0 0 1 340.7 659.3 L460.2 759.6 A52 52 0 0 0 448.2 788.5 Z"/>
      <path fill="var(--mid-blue)" d="M340.7 659.3 A208 208 0 0 1 439.2 594.1 L484.8 743.3 A52 52 0 0 0 460.2 759.6 Z"/>
      <path fill="var(--dark-gray)" d="M439.5 595 A207 207 0 0 1 500 586 L500 741 A52 52 0 0 0 484.8 743.3 Z"/>
    </g>
    <g class="rings" fill="none" stroke="#ffffff" stroke-width="1.2">
      <circle cx="500" cy="793" r="105"/>
      <circle cx="500" cy="793" r="158"/>
    </g>
    <circle cx="500" cy="793" r="51" fill="#ffffff"/>
    <text x="500" y="797" text-anchor="middle" font-size="17" font-weight="700" fill="var(--navy)">Clinora</text>

    <g class="values">
      <text class="seg-label" transform="translate(471 612) rotate(81)">8%</text>
      <text class="seg-label" transform="translate(396 643) rotate(56)">50%</text>
      <text class="seg-label" transform="translate(330 726) rotate(22)">19%</text>
      <text class="seg-label" transform="translate(343 888) rotate(-32)">18%</text>
      <text class="seg-label" transform="translate(643 681) rotate(-38)">50%</text>
      <text class="seg-label" transform="translate(456 728) rotate(60)">n = 70</text>
      <text class="seg-label" transform="translate(425 767) rotate(20)">n = 50</text>
      <text class="seg-label" transform="translate(432 836) rotate(-35)">n = 100</text>
      <text class="seg-label" transform="translate(563 746) rotate(-52)">n = 30</text>
      <text class="seg-label" transform="translate(535 864) rotate(62)">n = 20</text>
    </g>

    <g class="callouts">
      <polyline class="leader" points="476,592 503,556 545,556"/>
      <circle class="leader-dot" cx="476" cy="592" r="3.5"/>
      <text class="call-label" fill="var(--label-dark)" x="549" y="566">oxaliplatin/capecitabine</text>
      <text class="call-label" fill="var(--label-dark)" x="549" y="585">plus bevacizumab</text>

      <polyline class="leader" points="378,642 348,605 264,605"/>
      <circle class="leader-dot" cx="378" cy="642" r="3.5"/>
      <text class="call-label" fill="var(--mid-blue)" x="333" y="624" text-anchor="end">oxaliplatin/</text>
      <text class="call-label" fill="var(--mid-blue)" x="333" y="643" text-anchor="end">capecitabine</text>

      <polyline class="leader" points="308,737 274,764 140,764"/>
      <circle class="leader-dot" cx="308" cy="737" r="3.5"/>
      <text class="call-label" fill="var(--label-light-blue)" x="274" y="737" text-anchor="end">oxaliplatin/leucovorin/5-FU</text>
      <text class="call-label" fill="var(--label-light-blue)" x="274" y="756" text-anchor="end">plus bevacizumab</text>

      <polyline class="leader" points="370,849 285,922 216,922"/>
      <circle class="leader-dot" cx="370" cy="849" r="3.5"/>
      <text class="call-label" fill="var(--orange)" x="280" y="897" text-anchor="end">irinotecan/leucovorin/5-FU plus</text>
      <text class="call-label" fill="var(--orange)" x="280" y="916" text-anchor="end">bevacizumab</text>

      <polyline class="leader" points="486,919 515,1003 530,1003"/>
      <circle class="leader-dot" cx="486" cy="919" r="3.5"/>
      <text class="call-label" fill="var(--label-dark)" x="535" y="998">irinotecan</text>

      <polyline class="leader" points="614,651 664,615 752,615"/>
      <circle class="leader-dot" cx="614" cy="651" r="3.5"/>
      <text class="call-label" fill="var(--navy)" x="661" y="635">oxaliplatin/leucovorin/5-FU</text>

      <polyline class="leader" points="661,700 734,752 800,752"/>
      <circle class="leader-dot" cx="661" cy="700" r="3.5"/>
      <text class="call-label" fill="var(--navy)" x="734" y="723">irinotecan/leucovorin/5-FU</text>
      <text class="call-label" fill="var(--navy)" x="734" y="742">plus cetuximab</text>
    </g>
  </svg>
</div>
</body>
</html>
```